Copper Lantern LLC Business Card

We need a business card design for a newco in Texas. We are a team of professionals who join start ups as founders and help launch their businesses, which are primarily related to food and beverage and the service side of the industry. We love local and craft and are partners in businesses in the local meat, BBQ and Burger, fine dining, and beverage alcohol businesses. Our specialty is finance and the business side of start ups, including assisting with capital raises as principals, not brokers. We do not currently have any logos or graphics for this entity. Our values include helping people succeed, rooting for the underdog, healthy food, the environment and being good citizens.

Target Market(s)

Everybody but also Angel Investors, CPAs, Bankers, Entrepreneurs

Industry/Entity Type

Business

Contact Information for Business Card

Fields for Business Name, Title, Email Address, Phone Number. Place to add mailing address and web domain later.

Font styles to use
Sans Serif

Colors

Designer to choose colors to be used in the design.

Requirements
Should not have
• Pictures of booze bottles or drinks thought there could be a social scene that does not strictly focus on those. No cows, cowboy hats or ranches. We are not a Wall Street type entity so no huge office buildings or skylines.

```html
<!DOCTYPE html>
<html lang="en">
<head>
<meta charset="utf-8">
<title>Copper Lantern LLC Business Card</title>
<link href="https://fonts.googleapis.com/css2?family=Montserrat:wght@700&family=Roboto:wght@400;500&display=swap" rel="stylesheet">
<style>
  :root {
    --bg: #1c1c1e;
    --card-dark: #141414;
    --card-light: #ffffff;
    --ink: #1a1a1a;
    --red: #e31e24;
    --white: #ffffff;
  }
  * { margin: 0; padding: 0; box-sizing: border-box; }
  html, body { width: 1200px; height: 1200px; overflow: hidden; background: var(--bg); }
  .canvas { position: relative; width: 1200px; height: 1200px; }
  .card { position: absolute; left: 100px; width: 1000px; height: 540px; overflow: hidden; box-shadow: 0 18px 40px rgba(0,0,0,.5); }
  .card-back { top: 45px; background: var(--card-dark); }
  .card-front { top: 615px; background: var(--card-light); }

  .brand-dot { position: absolute; border-radius: 50%; }
  .card-back .brand-dot { width: 130px; height: 130px; left: 435px; top: 140px; background: var(--red); }
  .card-back .company { position: absolute; left: 0; width: 100%; top: 300px; text-align: center; font: 700 44px Montserrat, sans-serif; color: var(--white); }

  .card-front .brand-dot { width: 160px; height: 160px; left: 45px; top: 35px; background: var(--red); }
  .card-front .company { position: absolute; right: 70px; top: 140px; font: 700 44px Montserrat, sans-serif; color: var(--ink); }

  .person { position: absolute; left: 55px; top: 235px; }
  .person-name { font: 700 34px Montserrat, sans-serif; color: var(--ink); }
  .person-title { font: 400 19px Roboto, sans-serif; color: var(--red); margin-top: 2px; }
  .divider { position: absolute; left: 275px; right: 80px; top: 300px; height: 2px; background: var(--ink); }

  .contact { list-style: none; position: absolute; font: 400 21px Roboto, sans-serif; color: var(--ink); }
  .contact li { display: flex; align-items: center; gap: 14px; height: 36px; }
  .contact svg { width: 28px; height: 28px; flex: none; }
  .phones { left: 40px; top: 318px; }
  .online { right: 45px; top: 385px; }
  .online li { justify-content: flex-end; }

  .address { position: absolute; left: 250px; top: 462px; font: 400 21px Roboto, sans-serif; color: var(--ink); }
  .footer-band { position: absolute; left: 0; right: 0; bottom: 0; height: 40px; }
</style>
</head>
<body>
<main class="canvas">
  <section class="card card-back" aria-label="Card back">
    <span class="brand-dot"></span>
    <p class="company">Copper Lantern LLC</p>
  </section>

  <section class="card card-front" aria-label="Card front">
    <span class="brand-dot"></span>
    <p class="company">Copper Lantern LLC</p>

    <div class="person">
      <p class="person-name">Marcus Hale</p>
      <p class="person-title">Managing Director</p>
    </div>
    <div class="divider"></div>

    <ul class="contact phones">
      <li>
        <svg viewBox="0 0 28 28" fill="none" stroke="var(--red)" stroke-width="1.6"><circle cx="14" cy="14" r="12.5"/><path d="M8 12c0-2 2.5-3 6-3s6 1 6 3l-2 1-1-2h-6l-1 2zM10 14h8l1 5H9z"/></svg>
        <span>+61(8) 5550 1234</span>
      </li>
      <li>
        <svg viewBox="0 0 28 28" fill="none" stroke="var(--red)" stroke-width="1.6"><circle cx="14" cy="14" r="12.5"/><rect x="10" y="7" width="8" height="14" rx="1.5"/><path d="M12 17h4"/></svg>
        <span>+61(400) 555 019</span>
      </li>
    </ul>

    <ul class="contact online">
      <li>
        <span>marcushale@copperlantern.com</span>
        <svg viewBox="0 0 28 28" fill="none" stroke="var(--red)" stroke-width="1.6"><circle cx="14" cy="14" r="12.5"/><rect x="7.5" y="9.5" width="13" height="9"/><path d="M7.5 9.5l6.5 5 6.5-5"/></svg>
      </li>
      <li>
        <span>www.copperlantern.com</span>
        <svg viewBox="0 0 28 28" fill="none" stroke="var(--red)" stroke-width="1.6"><circle cx="14" cy="14" r="12.5"/><circle cx="14" cy="14" r="7"/><ellipse cx="14" cy="14" rx="3" ry="7"/><path d="M7 14h14"/></svg>
      </li>
    </ul>

    <p class="address">Suite 7/18 Harbour Rd, Eastbrook WA 6100</p>

    <svg class="footer-band" viewBox="0 0 1000 40" preserveAspectRatio="none" aria-hidden="true">
      <polygon points="0,0 760,0 775,40 0,40" fill="var(--ink)"/>
      <polygon points="770,0 1000,0 1000,40 785,40" fill="var(--red)"/>
    </svg>
  </section>
</main>
</body>
</html>
```